Marlowe Ridge Holdings

I have a real estate investment business.

** I need editable vector files of the final design.

Industry/Entity Type

Real Estate

Contact Information for Business Card

I would like the card to be clear and direct with the company name and contact info. I would prefer not to have a design that is too busy (i.e., with excessive detail) in the business card.

Font styles to use
Sans Serif

Requirements
Must have
• My card must have the following information listed below:
• Company name: Marlowe Ridge Holdings LLC
• My name: Daniel Vestrap
• Phone number: (555) 218-9064
• Email address: dlvestrap@fernmail.example
• Keywords: “Real Estate Investments”
Nice to have
• I would like to have a design that resembles the characteristics/uses of obsidian stone which resembles something related to strength and resilience. Perhaps something with sharp, sleek color transitions as well.

```html
<!DOCTYPE html>
<html lang="en">
<head>
<meta charset="UTF-8">
<title>Marlowe Ridge Holdings LLC — Business Card</title>
<link rel="stylesheet" href="https://fonts.googleapis.com/css2?family=Roboto+Condensed:wght@600&family=Montserrat:wght@400;500&display=swap">
<style>
  :root {
    --page-bg: #ffffff;
    --card-bg: #fbfbfb;
    --obsidian: #2b3a52;
    --slate: #6b7196;
    --ink: #3b3b3f;
    --rule: #3a3f4c;
  }
  html, body {
    margin: 0;
    padding: 0;
    width: 1200px;
    height: 1200px;
    overflow: hidden;
    background: var(--page-bg);
  }
  .card {
    position: absolute;
    left: 100px;
    top: 313px;
    width: 1000px;
    height: 573px;
    background: var(--card-bg);
    box-shadow: 0 0 0 1px #efefef;
    overflow: hidden;
  }
  .brand {
    position: absolute;
    left: 20px;
    width: 460px;
    top: 238px;
    text-align: center;
    font-family: "Roboto Condensed", "Arial Narrow", sans-serif;
    font-weight: 600;
  }
  .brand-name {
    margin: 0;
    font-size: 46px;
    line-height: 1;
    color: var(--obsidian);
    letter-spacing: -0.5px;
  }
  .brand-tagline {
    margin: 16px 0 0;
    font-size: 30px;
    line-height: 1;
    color: var(--slate);
  }
  .divider {
    position: absolute;
    left: 499px;
    top: 198px;
    width: 2px;
    height: 174px;
    background: var(--rule);
  }
  .contact {
    position: absolute;
    left: 557px;
    top: 190px;
    font-family: "Montserrat", sans-serif;
  }
  .person-name {
    margin: 0;
    font-size: 36px;
    font-weight: 500;
    line-height: 1.1;
    color: var(--slate);
    letter-spacing: 0.5px;
  }
  .person-title {
    margin: 2px 0 0;
    font-size: 28px;
    font-weight: 400;
    line-height: 1.2;
    color: var(--ink);
    letter-spacing: 0.5px;
  }
  .contact-list {
    list-style: none;
    margin: 40px 0 0;
    padding: 0;
  }
  .contact-item {
    display: flex;
    align-items: center;
    height: 38px;
    font-size: 23px;
    color: var(--ink);
    letter-spacing: 0.4px;
  }
  .contact-icon {
    width: 24px;
    height: 24px;
    margin-right: 21px;
    flex: none;
  }
  .base-band {
    position: absolute;
    left: 0;
    bottom: 0;
    width: 100%;
    height: 50px;
    background: linear-gradient(90deg, var(--obsidian) 0%, var(--obsidian) 49%, var(--slate) 51%, var(--slate) 100%);
  }
</style>
</head>
<body>
  <div class="card">
    <div class="brand">
      <h1 class="brand-name">Marlowe Ridge Holdings LLC</h1>
      <p class="brand-tagline">Real Estate Investments</p>
    </div>

    <div class="divider"></div>

    <div class="contact">
      <h2 class="person-name">Daniel Vestrap</h2>
      <p class="person-title">Manager</p>
      <ul class="contact-list">
        <li class="contact-item">
          <svg class="contact-icon" viewBox="0 0 24 24" aria-hidden="true">
            <path d="M9 3 L12 7 L10 9.5 C10.5 12 12 14 14.5 15 L17 13 L21 16 L18.5 20 C11 19.5 4.5 13 4 5.5 Z" fill="none" stroke="#6b7196" stroke-width="2" stroke-linejoin="round"/>
          </svg>
          (555) 218-9064
        </li>
        <li class="contact-item">
          <svg class="contact-icon" viewBox="0 0 24 24" aria-hidden="true">
            <rect x="2" y="5" width="20" height="14" fill="#6b7196"/>
            <path d="M2 5 L12 13 L22 5 M2 19 L9.5 11 M22 19 L14.5 11" fill="none" stroke="#fbfbfb" stroke-width="1.5"/>
          </svg>
          dlvestrap@fernmail.example
        </li>
      </ul>
    </div>

    <div class="base-band" role="img" aria-label="Band of slanted obsidian and slate blocks along the bottom edge"></div>
  </div>
</body>
</html>
```